Esport Center Food Menu

We need a cool food menu designed for our Esports facility, a place for people to play all the latest esport games and we serve food and drinks. It will be put on our website, printed and put on quality paper the size of printer paper and will be put on a television screen. We would like the colors to go well with our logo. Color scheme Red/Black/White/Light Gray/Dark Gray. Attached is the example we came up with, it has to look cooler than this! Our font is http://www.typorell.net/kovanteri.font

Industry/Entity Type

Games

Requirements
Must have
• Our logo in it, match our color scheme
Nice to have
• Our font is http://www.typorell.net/kovanteri.font
• We are having different beers that will be changed monthly. If there is a cool way to make these beers stand out, that would be nice to have.

```html
<!DOCTYPE html>
<html lang="en">
<head>
<meta charset="utf-8">
<title>Pixel Forge Cafe Menu</title>
<link href="https://fonts.googleapis.com/css2?family=Orbitron:wght@500;700&display=swap" rel="stylesheet">
<style>
  :root{
    --bg:#d9d6d2;
    --panel:#eceded;
    --ink:#1b1b1d;
    --dark-gray:#3b3c3f;
    --mid-gray:#6b6d71;
    --red:#d2232a;
    --white:#ffffff;
  }
  *{box-sizing:border-box;margin:0;padding:0}
  html,body{width:1200px;height:1000px;overflow:hidden;background:var(--bg)}
  .menu{
    position:absolute;left:237px;top:30px;width:726px;height:940px;
    display:flex;background:var(--panel);
    box-shadow:0 6px 24px rgba(0,0,0,.18);
    font-family:'Orbitron',sans-serif;color:var(--ink);
  }
  .photo-column{width:290px;height:100%;display:flex;flex-direction:column}
  .photo{flex:none}
  .photo--pasta{height:320px;background:linear-gradient(135deg,#1c2638 0%,#2a3850 40%,#6b4a3c 70%,#b4553a 100%)}
  .photo--pizza{height:305px;background:linear-gradient(160deg,#7a3a24 0%,#5a5a30 45%,#3f5a2e 65%,#2e3744 100%)}
  .photo--cones{height:95px;background:linear-gradient(180deg,#a87a48 0%,#c79a62 50%,#4a4f5a 100%)}
  .photo--icecream{height:220px;background:linear-gradient(180deg,#3a3f48 0%,#24262b 45%,#6e6558 75%,#cfc3ad 100%)}
  .info-panel{position:relative;flex:1;height:100%}
  .brand{
    position:absolute;left:0;right:0;top:70px;text-align:center;color:var(--dark-gray);
    font-weight:700;letter-spacing:2px;line-height:1.2;
  }
  .brand-mark{display:block;width:34px;height:34px;border-radius:50%;background:var(--red);margin:0 auto 18px}
  .brand-name{font-size:22px}
  .brand-sub{font-size:34px}
  .section-label{
    position:absolute;width:40px;background:var(--dark-gray);
    border:2px solid var(--red);color:var(--white);
    display:flex;align-items:center;justify-content:center;
  }
  .section-label span{writing-mode:vertical-rl;font-size:16px;letter-spacing:5px;font-weight:500}
  .section-label--right{right:18px}
  .section-label--left{left:18px}
  .pointer{position:absolute;width:22px}
  .item-list{
    position:absolute;left:70px;right:70px;list-style:none;text-align:center;
    font-size:14px;font-weight:500;line-height:18px;letter-spacing:.5px;
  }
  .note{position:absolute;left:70px;right:70px;text-align:center;font-size:7px;letter-spacing:1px;color:var(--mid-gray)}
</style>
</head>
<body>
<main class="menu">
  <div class="photo-column">
    <div class="photo photo--pasta" role="img" aria-label="Plate of spaghetti with tomatoes and toasted bread"></div>
    <div class="photo photo--pizza" role="img" aria-label="Flatbread pizza with vegetables and basil"></div>
    <div class="photo photo--cones" role="img" aria-label="Waffle ice cream cones"></div>
    <div class="photo photo--icecream" role="img" aria-label="Bowl of ice cream scoops with cinnamon sticks"></div>
  </div>

  <section class="info-panel">
    <header class="brand">
      <span class="brand-mark"></span>
      <div class="brand-name">PIXEL FORGE</div>
      <div class="brand-sub">CAFE</div>
    </header>

    <div class="section-label section-label--right" style="top:240px;height:146px"><span>PANINI</span></div>
    <svg class="pointer" style="right:60px;top:250px;height:126px" viewBox="0 0 22 126"><polygon points="22,0 0,63 22,126 14,63" fill="var(--ink)"/></svg>
    <ul class="item-list" style="top:290px">
      <li>BUFFALO CHICKEN</li><li>HAM &amp; CHEESE</li><li>BBQ CHICKEN</li><li>TURKEY SWISS</li>
    </ul>

    <div class="section-label section-label--left" style="top:408px;height:170px"><span>AIR FRIED</span></div>
    <svg class="pointer" style="left:60px;top:418px;height:150px" viewBox="0 0 22 150"><polygon points="0,0 22,75 0,150 8,75" fill="var(--ink)"/></svg>
    <p class="note" style="top:425px">FULL OR HALF ORDER</p>
    <ul class="item-list" style="top:440px">
      <li>CHICKEN TENDERS</li><li>FRIED PICKLES</li><li>FRIES</li><li>LOADED FRIES</li>
    </ul>
    <p class="note" style="top:515px">ASSORTED SNACKS ALSO AVAILABLE</p>

    <div class="section-label section-label--right" style="top:540px;height:140px"><span>DRINKS</span></div>
    <svg class="pointer" style="right:60px;top:550px;height:120px" viewBox="0 0 22 120"><polygon points="22,0 0,60 22,120 14,60" fill="var(--ink)"/></svg>
    <ul class="item-list" style="top:578px;font-size:13px">
      <li>VOLT RUSH ENERGY DRINK</li><li>PIXEL FORGE BLEND COFFEE</li><li>CHAI OR GREEN TEA LATTE</li><li>SODA</li>
    </ul>

    <div class="section-label section-label--left" style="top:695px;height:190px"><span>BUBBLE TEA</span></div>
    <svg class="pointer" style="left:60px;top:705px;height:170px" viewBox="0 0 22 170"><polygon points="0,0 22,85 0,170 8,85" fill="var(--ink)"/></svg>
    <ul class="item-list" style="top:712px">
      <li>MANGO</li><li>HONEYDEW</li><li>BLUE RASPBERRY</li><li>TARO</li><li>STRAWBERRY</li><li>ORANGE CREAM</li>
    </ul>
  </section>
</main>
</body>
</html>
```